Dunmore Associates Banner Add

We are an international headhunting firm looking to target IT guys in Europe and USA to come and work in Singapore or Sydney (Australia). These guys will generally work in Trading firms / Banks / Top Tech Firms. Text - "Are you working in the Fin/ Tech space for a bank or High Frequency Trading firm as a technologist?We have your job in Singapore/ Sydney.Better / Great LifestyleWorking visa'sThe highest calibre clients.Bored with Brexit?Apply now.We need 5 pictures to rotate on a banner add to attract attention / represent this call to action.Some ideas… Guy on a laptop on a beach Sydney Skyline Singapore Skyline Bondi Beach Paradise beach picturesPeople playing on Beach London in the rain vs Sydney (sunny)Style needs to be classy, premium, well finished, boutique and in keeping with our website www.dunmore-associates-example.net. - hence any text you think could be worthwhile taking from there is fine.File formats: JPG, PNG, GIF Maximum file size: 3MB Media Sizes: Minimum: 600 × 315 pixels Recommended: 1200 × 628 pixels Image ratio: 1.91:1 To maximize advert delivery, Images need to be public property, no copyright. 5 rotating pictures incorporating the text, pictures and sell to create one banner add.

Target Market(s)

Banking/ Finance

Number of Pages Required

1 page

Requirements
Must have
• 5 different banners on rotate
Nice to have
• Classy, text suggested or snippets of as required, maybe black and white to match our logo's but injections of colour but full colour is also fine I could be converted.
Should not have
• not too flashy, should be elegant, classy pictures, clean like our website.
• www.dunmore-associates-example.net

```html
<!DOCTYPE html>
<html lang="en">
<head>
<meta charset="utf-8">
<title>Dunmore Associates – Banner</title>
<link rel="stylesheet" href="https://fonts.googleapis.com/css2?family=Oswald:wght@400;500&family=Cinzel:wght@500&family=Roboto:wght@500&display=swap">
<style>
  :root {
    --page-bg: #e4e6e8;
    --brand-yellow: #fbd921;
    --charcoal: #2b2b2b;
    --ink: #232323;
    --photo-light: #4a4a4a;
    --photo-dark: #262626;
  }
  * { box-sizing: border-box; margin: 0; padding: 0; }
  html, body {
    width: 1200px; height: 1200px; overflow: hidden;
    background: var(--page-bg);
  }
  .canvas { position: relative; width: 1200px; height: 1200px; }
  .banner {
    position: absolute; left: 20px; top: 298px;
    width: 1160px; height: 604px;
    background: var(--brand-yellow);
    overflow: hidden;
  }
  .banner__shapes { position: absolute; inset: 0; width: 100%; height: 100%; }
  .banner__photo {
    position: absolute; left: 780px; top: 6px; width: 360px; height: 598px;
    background: linear-gradient(180deg, var(--photo-light) 0%, var(--photo-dark) 100%);
  }
  .brand {
    position: absolute; left: 68px; width: 400px; top: 140px;
    text-align: center; color: var(--ink);
  }
  .brand__name {
    font-family: "Cinzel", serif; font-weight: 500;
    font-size: 18px; letter-spacing: 3px; text-transform: uppercase;
  }
  .brand__tagline {
    font-family: "Cinzel", serif; font-weight: 500;
    font-size: 6.5px; letter-spacing: 1.6px; text-transform: uppercase;
    margin-top: 4px;
  }
  .pitch {
    position: absolute; left: 18px; width: 500px; top: 262px;
    text-align: center; color: var(--ink);
    font-family: "Oswald", sans-serif; font-weight: 500;
    font-variant: small-caps; font-size: 42px; line-height: 46px;
  }
  .hook {
    position: absolute; left: 68px; width: 400px; top: 430px;
    text-align: center; color: var(--ink);
    font-family: "Oswald", sans-serif; font-weight: 500;
    font-variant: small-caps; font-size: 48px; line-height: 54px;
  }
  .hook__rule {
    position: absolute; left: 88px; top: 486px; width: 357px;
    border-top: 2px dashed var(--ink);
  }
  .cta {
    position: absolute; left: 361px; top: 533px; width: 218px; height: 52px;
    border: 2px solid var(--ink); border-radius: 4px;
    display: flex; align-items: center; justify-content: center;
    font-family: "Roboto", sans-serif; font-weight: 500; font-size: 25px;
    color: var(--ink);
  }
</style>
</head>
<body>
<div class="canvas">
  <section class="banner">
    <svg class="banner__shapes" viewBox="0 0 966 503" preserveAspectRatio="none" aria-hidden="true">
      <path fill="var(--charcoal)" d="M638,0 H966 V503 H525 L391,121 L538,405 C560,250 620,120 688,61 Z"/>
    </svg>
    <div class="banner__photo" role="img" aria-label="Photo of a professional in a black tuxedo and bow tie"></div>

    <div class="brand">
      <div class="brand__name">Dunmore Associates</div>
      <div class="brand__tagline">Boutique Executive Search</div>
    </div>

    <div class="pitch">
      Better / Great Lifestyle<br>
      Working visa's<br>
      The highest calibre clients.
    </div>

    <div class="hook">Bored with Brexit?</div>
    <div class="hook__rule"></div>

    <div class="cta">Apply Now</div>
  </section>
</div>
</body>
</html>
```